Modernise Business Card

Our company has been operating for 10 years. With the start of the new decade we are looking to refresh our business card design. We manufacture a range of industrial product shipping to customers internationally. A copy of our current card, both sides, is attached. We are looking for a mature professional appearance.

```html
<!DOCTYPE html>
<html lang="en">
<head>
<meta charset="utf-8">
<title>Corvane Business Card</title>
<link rel="stylesheet" href="https://fonts.googleapis.com/css2?family=Cabin:wght@400;500;700&display=swap">
<style>
  :root {
    --bg: #e8e9eb;
    --card: #ffffff;
    --charcoal: #333233;
    --text: #3a3a3c;
    --blue-deep: #0f60b0;
    --blue-light: #00aed8;
    --white: #ffffff;
  }
  * { box-sizing: border-box; margin: 0; padding: 0; }
  html, body {
    width: 1200px; height: 1200px; overflow: hidden;
    background: var(--bg);
    font-family: "Cabin", "Gill Sans", sans-serif;
  }
  .card {
    position: absolute;
    width: 836px; height: 478px;
    background: var(--card);
    overflow: hidden;
  }
  .card-front { left: 182px; top: 60px; }
  .card-back { left: 182px; top: 637px; }

  .brand-name {
    position: absolute;
    font-weight: 700;
    color: var(--blue-light);
    line-height: 1;
    letter-spacing: 0.5px;
  }
  .tagline {
    position: absolute;
    color: var(--text);
    font-weight: 400;
    line-height: 1.25;
    text-transform: uppercase;
  }

  /* front */
  .front-band {
    position: absolute; left: 0; right: 0; top: 282px; bottom: 0;
    background: linear-gradient(90deg, var(--charcoal) 0%, var(--blue-deep) 35%, var(--blue-light) 100%);
  }
  .card-front .brand-name { left: 0; right: 0; top: 112px; text-align: center; font-size: 52px; }
  .card-front .tagline { left: 0; right: 0; top: 176px; text-align: center; font-size: 22px; line-height: 32px; }
  .front-web {
    position: absolute; right: 18px; bottom: 8px;
    color: var(--white); font-size: 16px; font-weight: 700;
  }

  /* back */
  .back-panel {
    position: absolute; left: 0; top: 0; bottom: 0; width: 372px;
    background: var(--charcoal);
  }
  .back-band {
    position: absolute; left: 372px; top: 0; bottom: 0; width: 96px;
    background: linear-gradient(90deg, var(--blue-deep) 0%, var(--blue-light) 100%);
  }
  .holder-name {
    position: absolute; left: 36px; top: 62px;
    color: var(--white); font-size: 30px; font-weight: 700;
  }
  .contact-list { position: absolute; left: 28px; top: 182px; list-style: none; }
  .contact-item {
    display: flex; align-items: center;
    height: 40px; margin-bottom: 18px;
    color: var(--white); font-size: 13px; line-height: 17px;
  }
  .contact-item:nth-child(2) { margin-bottom: 20px; }
  .contact-icon {
    flex: none; width: 40px; height: 40px; border-radius: 50%;
    background: var(--white); margin-right: 22px;
    display: flex; align-items: center; justify-content: center;
  }
  .contact-icon svg { width: 22px; height: 22px; }
  .card-back .brand-name { right: 22px; top: 188px; font-size: 50px; text-align: right; }
  .card-back .tagline { right: 26px; top: 254px; font-size: 16.5px; line-height: 27px; text-align: right; }
</style>
</head>
<body>

<section class="card card-front" aria-label="Card front">
  <div class="front-band" role="img" aria-label="Decorative blue wave band along the bottom of the card"></div>
  <div class="brand-name">Corvane</div>
  <p class="tagline">Hydraulic Adapters House Fittings<br>Quick Couplings</p>
  <div class="front-web">www.corvanefittings.com</div>
</section>

<section class="card card-back" aria-label="Card back">
  <div class="back-panel"></div>
  <div class="back-band" role="img" aria-label="Decorative vertical blue wave band dividing the card"></div>

  <h1 class="holder-name">Glen Harper</h1>

  <ul class="contact-list">
    <li class="contact-item">
      <span class="contact-icon"><svg viewBox="0 0 24 24"><path d="M12 2a7 7 0 0 0-7 7c0 5 7 13 7 13s7-8 7-13a7 7 0 0 0-7-7zm0 9.5A2.5 2.5 0 1 1 12 6.5a2.5 2.5 0 0 1 0 5z" fill="var(--charcoal)"/></svg></span>
      <span>1208-4, Lumen Tower 88 Riverside Road,<br>Harbour District Eastport 300200 China</span>
    </li>
    <li class="contact-item">
      <span class="contact-icon"><svg viewBox="0 0 24 24"><rect x="3" y="6" width="18" height="12" fill="none" stroke="var(--charcoal)" stroke-width="2"/><path d="M3 6l9 7 9-7" fill="none" stroke="var(--charcoal)" stroke-width="2"/></svg></span>
      <span>gharper@corvanefittings.com</span>
    </li>
    <li class="contact-item">
      <span class="contact-icon"><svg viewBox="0 0 24 24"><path d="M6.6 10.8a15 15 0 0 0 6.6 6.6l2.2-2.2a1 1 0 0 1 1-.25 11.4 11.4 0 0 0 3.6.57 1 1 0 0 1 1 1V20a1 1 0 0 1-1 1A17 17 0 0 1 3 4a1 1 0 0 1 1-1h3.5a1 1 0 0 1 1 1c0 1.250.2 2.45.57 3.57a1 1 0 0 1-.25 1z" fill="var(--charcoal)"/></svg></span>
      <span>China: +86 100 2000 3456<br>Australia: +61 400 123 789</span>
    </li>
    <li class="contact-item">
      <span class="contact-icon"><svg viewBox="0 0 24 24" fill="none" stroke="var(--charcoal)" stroke-width="1.8"><circle cx="12" cy="12" r="9"/><ellipse cx="12" cy="12" rx="4" ry="9"/><path d="M3 12h18M5 7h14M5 17h14"/></svg></span>
      <span>www.corvanefittings.com</span>
    </li>
  </ul>

  <div class="brand-name">Corvane</div>
  <p class="tagline">Hydraulic Adapters House Fittings<br>Quick Couplings</p>
</section>

</body>
</html>
```